Kovri DIGITAL HORIZON learning portal

We beed a flyer design to launch our new DIGITAL HORIZON Learning Portal. The flyer will be used in letter box drops and to give to small business to encourage sales of this new service.

ABOUT US:

We are a small training firm offering world class training solutions in the areas of:

1. Time Management
2. Sales skills
3. Strategic & High performance leadership
4. Sales Management
5. Personal Maximum Achievement.

You can find our website at www.kovri.com.au

ABOUT DIGITAL HORIZON Learning Portal:

We are launching an online learning portal called DIGITAL HORIZON Learning Portal which will allow anyone, anywhere in the world to take our courses online as long as they have access to a PC, smart phone and internet.

Taking an online course with Kovri through our DIGITAL HORIZON Learning Portal will allow students/participants to save over 50% of the normal price of attending a face to face training program.

There are over 80 different individual learning units that can be taken by a student/participant. The participant can choose to take any unit they wish building their own unique learning experience or they can take a full course in one of the subject areas listed above in the about us section.

ADVANTAGES OF USING THE Kovri DIGITAL HORIZON Learning Portal:

* Cost effective, save over 50% by learning online compared to attending a Kovri class room based programme.
* learning can be scheduled around work and family
* Reduces travel time and travel costs
* Students/participants have the option to select learning materials that meets their level of knowledge and interest.
* Complete flexibility to build a personalised learning experience.
* Students/participants can study anywhere they have access to a computer and Internet connection
* Self-paced learning modules allow students/participants to work at their own pace
* Develops knowledge of the Internet and computers skills that will help learners throughout their lives and careers
* Successfully completing online or computer-based courses builds self-knowledge and self-confidence and encourages students to take responsibility for their learning
* Join over 4 million people who have successfully undertaken the training world wide at a time & a place convenient to students/participants.
* pay securely using zentrapay
* learn based on a students/participants personal financial circumstances with individual units priced at $82.50 each (this is Australian dollars & includes GST)

The final design will be one that conveys flexibility of learning, cost effectiveness of the online learning solution. The flyer design can either be folded, single or double sided, A4 or A5 or DL size - whatever works best in the final outcome.

Industry/Entity Type

Small Business

Requirements
Must have
• The flyer must include:

* the "DIGITAL HORIZON Learning portal" logo and the "Kovri logo" and use the Kovri font. Several logos have been provided and the most appropriate ones can be chosen for the design. The font has been provided. (I do have other logo files in different file formats if required to aid designers)

* The flyer must direct people to the Kovri website www.kovri.com.au to pay, enrol and find out other information about the courses.

* The flyer must highlight cost effectiveness of the solution, the world wide popularity of the programs (over 4 million people have completed the programs world wide), flexibility of learning & the diversity of study areas.

Because of price changes in future of courses it would be very beneficial to be able to edit files in future to show new prices if and when that happens.

```html
<!DOCTYPE html>
<html lang="en">
<head>
<meta charset="utf-8">
<title>Kovri DIGITAL HORIZON Learning Portal – Flyers</title>
<link rel="stylesheet" href="https://fonts.googleapis.com/css2?family=Rokkitt:wght@700&family=Sacramento&family=Raleway:wght@400;600&family=Oswald:wght@600&display=swap">
<style>
  :root {
    --brand-blue: #2a8db8;
    --brand-blue-light: #4fb0d8;
    --brand-blue-dark: #1f6e93;
    --ink: #3d3d3d;
    --grey: #8a8f94;
    --paper: #ffffff;
    --backdrop: #e9ecef;
  }
  * { box-sizing: border-box; margin: 0; padding: 0; }
  html, body { width: 1200px; height: 1000px; overflow: hidden; }
  body {
    background: var(--backdrop);
    font-family: "Raleway", Arial, sans-serif;
    color: var(--ink);
    position: relative;
  }
  .flyer {
    position: absolute;
    top: 160px;
    width: 480px;
    height: 680px;
    background: var(--paper);
    box-shadow: 0 4px 16px rgba(0,0,0,.15);
    overflow: hidden;
  }
  .flyer--horizon { left: 90px; }
  .flyer--career { left: 630px; }

  .flyer__header {
    position: absolute; top: 0; left: 0; right: 0; height: 70px;
    background: var(--brand-blue);
    color: #fff;
    font-family: "Rokkitt", Georgia, serif;
    font-weight: 700;
    font-size: 44px;
    letter-spacing: .5px;
    text-align: center;
    line-height: 70px;
  }
  .flyer__photo {
    position: absolute; top: 70px; left: 0; right: 0; height: 280px;
  }
  .flyer--horizon .flyer__photo {
    background: linear-gradient(180deg, #f4f6f5 0%, #dde6e4 35%, #a9cde0 75%, #7fb6d4 100%);
  }
  .flyer--career .flyer__photo {
    background: linear-gradient(180deg, #f2f2f0 0%, #dcdad5 40%, #8c8a86 70%, #d9d7d2 100%);
  }
  .flyer__script {
    position: absolute; top: 62px; right: 30px;
    font-family: "Sacramento", cursive;
    font-size: 66px;
    color: var(--brand-blue);
    line-height: 1;
  }
  .flyer__benefits {
    position: absolute; top: 286px; left: 12px;
    list-style: none;
  }
  .flyer__benefits li {
    display: table;
    background: var(--brand-blue);
    color: #fff;
    font-size: 11.5px;
    font-weight: 600;
    padding: 2px 5px;
    margin-bottom: 5px;
  }
  .flyer__pitch {
    position: absolute; top: 372px; left: 36px; width: 200px;
    font-size: 15.5px;
    line-height: 1.3;
  }
  .portal-name {
    position: absolute; top: 375px; left: 262px; width: 190px; height: 36px;
    display: flex; align-items: center; gap: 8px;
    font-family: "Oswald", Arial, sans-serif;
    font-weight: 600; font-size: 19px; color: #2b3440;
  }
  .portal-name__mark { width: 16px; height: 16px; background: #2b3440; flex: none; }
  .offer {
    position: absolute; top: 410px; left: 238px; width: 170px; height: 120px;
  }
  .offer svg { position: absolute; inset: 0; }
  .offer__text {
    position: absolute; inset: 10px 10px 18px 10px;
    display: flex; flex-direction: column; align-items: center; justify-content: center;
    color: #fff; text-align: center; font-weight: 600;
    font-size: 9.5px; line-height: 1.15;
  }
  .offer__headline { font-size: 21px; font-weight: 600; line-height: 1.1; }
  .offer__price { font-size: 20px; line-height: 1; margin-top: 2px; }
  .flyer__cta {
    position: absolute; top: 478px; left: 34px;
    font-size: 15px;
  }
  .flyer__url {
    position: absolute; top: 505px; left: 34px;
    background: var(--brand-blue);
    color: #fff; font-weight: 600; font-size: 14.5px;
    padding: 2px 5px;
  }
  .brand {
    position: absolute; top: 590px; right: 34px;
    display: flex; align-items: center; gap: 7px;
    font-size: 22px; font-weight: 600; color: var(--grey);
  }
  .brand__mark { width: 20px; height: 20px; background: var(--brand-blue); }
</style>
</head>
<body>

<article class="flyer flyer--horizon">
  <h1 class="flyer__header">Expand your</h1>
  <div class="flyer__photo" role="img" aria-label="Photo of young adults relaxing on blue bean bags studying with a laptop and books"></div>
  <div class="flyer__script">horizon</div>
  <ul class="flyer__benefits">
    <li>Study online and upgrade your skills</li>
    <li>Gain anytime, anywhere access for complete flexibility</li>
    <li>Embrace lifelong learning and achieve more</li>
  </ul>
  <p class="flyer__pitch">Join over 4 million people who have completed online programs with Kovri.</p>
  <div class="portal-name"><span class="portal-name__mark"></span>DIGITAL HORIZON</div>
  <div class="offer">
    <svg viewBox="0 0 170 120" aria-hidden="true">
      <defs><linearGradient id="cloudA" x1="0" y1="0" x2="0" y2="1"><stop offset="0" stop-color="#5bbbe2"/><stop offset="1" stop-color="#2a86b5"/></linearGradient></defs>
      <ellipse cx="88" cy="112" rx="62" ry="7" fill="rgba(0,0,0,.12)"/>
      <path d="M20 40 C10 20 40 5 60 14 C72 0 100 2 110 14 C130 4 160 18 150 40 C168 52 160 78 142 80 C140 102 110 110 96 100 C84 114 56 112 48 98 C22 104 8 80 20 70 C4 60 8 44 20 40 Z" fill="url(#cloudA)"/>
    </svg>
    <div class="offer__text">
      <span class="offer__headline">Save 50%</span>
      <span>off the normal price of<br>face-to-face training.</span>
      <span style="margin-top:3px">From</span>
      <span class="offer__price">$82.50</span>
      <span>per unit</span>
    </div>
  </div>
  <p class="flyer__cta">Learn more at</p>
  <p class="flyer__url">www.kovri.com.au</p>
  <div class="brand"><span class="brand__mark"></span>Kovri</div>
</article>

<article class="flyer flyer--career">
  <h1 class="flyer__header">Makeover your</h1>
  <div class="flyer__photo" role="img" aria-label="Photo of a businesswoman seated at an outdoor cafe table with a laptop in front of a building"></div>
  <div class="flyer__script">career</div>
  <ul class="flyer__benefits">
    <li>Learn to be a great leader</li>
    <li>Polish your sales skills</li>
    <li>Improve performance at work</li>
  </ul>
  <p class="flyer__pitch">Fit your study around your work and family. Complete flexibility and personalised to your learning needs.</p>
  <div class="portal-name"><span class="portal-name__mark"></span>DIGITAL HORIZON</div>
  <div class="offer">
    <svg viewBox="0 0 170 120" aria-hidden="true">
      <defs><linearGradient id="cloudB" x1="0" y1="0" x2="0" y2="1"><stop offset="0" stop-color="#5bbbe2"/><stop offset="1" stop-color="#2a86b5"/></linearGradient></defs>
      <ellipse cx="88" cy="112" rx="62" ry="7" fill="rgba(0,0,0,.12)"/>
      <path d="M20 40 C10 20 40 5 60 14 C72 0 100 2 110 14 C130 4 160 18 150 40 C168 52 160 78 142 80 C140 102 110 110 96 100 C84 114 56 112 48 98 C22 104 8 80 20 70 C4 60 8 44 20 40 Z" fill="url(#cloudB)"/>
    </svg>
    <div class="offer__text">
      <span class="offer__headline">Over 80</span>
      <span>different learning units<br>for you to choose from<br>or undertake a<br>full course.</span>
    </div>
  </div>
  <p class="flyer__cta">Learn more at</p>
  <p class="flyer__url">www.kovri.com.au</p>
  <div class="brand"><span class="brand__mark"></span>Kovri</div>
</article>

</body>
</html>
```